Design needed for an A5 Flyer and Newspaper Ad

We are looking for a designer who can create us two graphical files. One is a flyer and one is a newspaper ad. Both have the same content. They just have a different format. Both the flyer and the ad should be in an adobe format.

Size:
Flyer format: A5
Newspaper format: 16 cm x 8 cm

The attached file Advertisement_KWT.indd is an ad of us for a different topic. But there is our logo in it.
We want you to create an ad and the flyer for gold purchase. I addes a file of a flyer from a competitor (1036 x 733.jpg). It can be made similar if you like. The file you make must be adjustable.

What needs to be on it:
Our Logo (Velten Haager AG)
Our address: Lindenweg 7, 4222 Zwingen
Since 1922

Font styles to use
Sans Serif

```html
<!DOCTYPE html>
<html lang="de">
<head>
<meta charset="utf-8">
<title>Velten Haager AG – Wir kaufen Gold</title>
<link href="https://fonts.googleapis.com/css2?family=PT+Sans+Narrow:wght@400;700&display=swap" rel="stylesheet">
<style>
  :root {
    --gold: #b98424;
    --gold-light: #e9c56a;
    --gold-deep: #8a5e14;
    --brand-red: #d8141c;
    --paper: #ffffff;
  }
  html, body { margin: 0; padding: 0; overflow: hidden; }
  body { width: 1200px; height: 892px; background: var(--paper); }
  .flyer {
    position: relative; width: 1200px; height: 892px; overflow: hidden;
    background: var(--paper);
    font-family: "PT Sans Narrow", "Arial Narrow", sans-serif;
    color: var(--gold); font-weight: 700;
  }
  .jewelry-photo {
    position: absolute; left: 22px; top: 190px; width: 655px; height: 385px;
    background:
      radial-gradient(ellipse 38% 42% at 40% 45%, #d9a640 0%, #c99234 45%, rgba(233,197,106,0.6) 72%, rgba(255,255,255,0) 100%),
      radial-gradient(ellipse 30% 30% at 72% 62%, rgba(233,197,106,0.8) 0%, rgba(255,255,255,0) 100%);
  }
  .brand {
    position: absolute; left: 120px; top: 595px;
    display: flex; align-items: center; gap: 16px;
    color: var(--brand-red); font-size: 54px; letter-spacing: 1px;
  }
  .brand-mark { width: 34px; height: 34px; background: var(--brand-red); }
  .since {
    position: absolute; left: 302px; top: 698px; transform: translateX(-50%);
    font-size: 25px; font-weight: 400; color: var(--gold);
  }
  .headline {
    position: absolute; left: 681px; top: 152px; margin: 0;
    font-size: 74px; line-height: 1;
  }
  .offer { position: absolute; margin: 0; font-size: 40px; line-height: 1; white-space: nowrap; }
  .offer-1a { left: 727px; top: 254px; }
  .offer-1b { left: 867px; top: 294px; }
  .offer-2a { left: 704px; top: 347px; }
  .offer-2b { left: 778px; top: 387px; }
  .divider {
    position: absolute; left: 815px; top: 516px; width: 132px; height: 0;
    border-top: 1.5px solid var(--gold);
  }
  .contact {
    position: absolute; left: 880px; top: 553px; transform: translateX(-50%);
    margin: 0; font-style: normal; text-align: center;
    font-size: 26px; line-height: 29px; white-space: nowrap;
  }
  .coins { position: absolute; left: 1028px; top: 690px; width: 165px; height: 175px; }
</style>
</head>
<body>
<main class="flyer">
  <div class="jewelry-photo" role="img" aria-label="Photo of a heap of gold jewellery: bangles, chains and rings"></div>

  <div class="brand">
    <span class="brand-mark"></span>
    <span class="brand-name">VELTEN HAAGER</span>
  </div>
  <div class="since">seit 1922</div>

  <h1 class="headline">Wir kaufen</h1>
  <p class="offer offer-1a">• Verschiedene Gold</p>
  <p class="offer offer-1b">und Silbermünzen</p>
  <p class="offer offer-2a">• Goldvreneli</p>
  <p class="offer offer-2b">und altes Gold</p>

  <div class="divider"></div>

  <address class="contact">
    VELTEN HAAGER AG<br>
    Philatelie und Numismatik<br>
    Lindenweg 7, 4299 Eichwil (Schweiz)<br>
    Tel. 0041 61 555 20 40<br>
    info@velten-haager.ch<br>
    www.velten-haager.ch
  </address>

  <svg class="coins" viewBox="0 0 170 180" role="img" aria-label="Photo of two historic gold coins">
    <defs>
      <radialGradient id="coin-tone" cx="40%" cy="35%" r="70%">
        <stop offset="0%" stop-color="#f0d58a"/>
        <stop offset="60%" stop-color="#c99a3c"/>
        <stop offset="100%" stop-color="#8a5e14"/>
      </radialGradient>
    </defs>
    <circle cx="113" cy="55" r="53" fill="url(#coin-tone)"/>
    <circle cx="62" cy="112" r="62" fill="url(#coin-tone)"/>
  </svg>
</main>
</body>
</html>
```